Letterhead Design for Law Firm

**Edit: I have added the photo of a bottom that I like.

------
We are looking for a re-design of our new letterhead. The letterhead is for a law firm and will be used for digital and traditionally printed correspondence.

Here are some suggestions:

- Please use colours are #8ec900 and simple black.
- Please do not use any type of "waves" at the bottom of the page. This is not in style at all.
- Please stay modern yet conservative.
- Please use font Segoe UI Light or similar if you can
- Avoid clipart or illustrations.
- Utilize ample white space in the layout so the design looks clean and information is easy to read at a glance. Don't overcrowd the letterhead.
- Make sure the letterhead design is consistent with our brand identity (see brambleford.ca)
-Please, no black headers or footers.

I am attaching my current letterhead and signature for your convenience.

Remember, the letterhead is an extension of our professional identity. We are a successful firm and trial lawyers who correspond with insurers, judges, lawyers, courts, clients, etc. Make it new, modern, attractive, yet powerful and conservative.

It needs to be easily printable. I would like the bleed removed in print so the black bar the bottom crosses the page (but the text is not near the edges)

Target Market(s)

Clients, Government Offices, Judiciary, Lawyers, Insurance Companies, Colleagues.

Industry/Entity Type

Law

Font styles to use
Other font styles liked:
• Segoe UI LIght, Calibri Light,

Colors
00AB8E
00BBA5
67D7C9
C6EFE9
E9F9F6

Requirements
Must have
• Everything that is on the letterhead now.
Nice to have
• Cutting Edge design, yet conservative.
Should not have
• law firm cliche design, images,

```html
<!DOCTYPE html>
<html lang="en">
<head>
<meta charset="utf-8">
<title>Brambleford Letterhead</title>
<link rel="stylesheet" href="https://fonts.googleapis.com/css2?family=Arimo:wght@400;700&family=Didact+Gothic&display=swap">
<style>
:root{
  --green:#8ec63f;
  --black:#000000;
  --ink:#4d4d4d;
  --rule:#bdbdbd;
  --paper:#ffffff;
  --backdrop:#dedede;
}
*{margin:0;padding:0;box-sizing:border-box}
html,body{width:1189px;height:1200px;overflow:hidden;background:var(--backdrop)}
.letterhead{position:absolute;left:184px;top:20px;width:820px;height:1160px;background:var(--paper);overflow:hidden;font-family:"Arimo",Arial,sans-serif;color:var(--ink)}
.brand{position:absolute;left:73px;top:58px;width:222px;text-align:center;color:var(--black)}
.brand-name{font-weight:400;font-size:28px;letter-spacing:.5px;line-height:34px;white-space:nowrap}
.brand-tagline{font-size:11px;letter-spacing:1.5px;line-height:14px;margin-top:6px;white-space:nowrap}
.divider{position:absolute;top:61px;width:1px;height:52px;background:var(--rule)}
.divider.first{left:338px}
.divider.second{left:526px}
.contact{position:absolute;left:382px;top:62px;list-style:none;font-size:12.5px;line-height:16px}
.contact li{display:flex;align-items:center;gap:5px;white-space:nowrap}
.contact svg{width:10px;height:10px;flex:none}
.address{position:absolute;left:563px;top:62px;font-size:12.5px;line-height:16px;font-style:normal;white-space:nowrap}
.salutation{position:absolute;left:74px;top:355px;font-family:"Didact Gothic",sans-serif;font-weight:700;font-size:19px;line-height:26px;color:var(--ink)}
.body-copy{position:absolute;left:73px;top:410px;width:680px;font-size:13.5px;line-height:17px;white-space:nowrap}
.body-copy p{margin-bottom:14.5px}
.closing{position:absolute;left:74px;top:756px;font-family:"Didact Gothic",sans-serif;font-weight:700;font-size:11px;line-height:14px}
.signature-mark{position:absolute;left:487px;top:857px;width:246px;height:58px;background:linear-gradient(90deg,#f2f2f2,#e6e6e6)}
.signatory{position:absolute;left:487px;top:924px;font-size:12.5px;line-height:16px;white-space:nowrap}
.signatory-name{color:var(--green);font-weight:700}
.footer-bar{position:absolute;left:0;width:820px}
.footer-bar.black{bottom:66px;height:8px;background:var(--black)}
.footer-bar.green{bottom:0;height:62px;background:var(--green)}
</style>
</head>
<body>
<main class="letterhead">
  <header>
    <div class="brand">
      <div class="brand-name">BRAMBLEFORD</div>
      <div class="brand-tagline">PERSONAL INJURY LAWYERS</div>
    </div>
    <span class="divider first"></span>
    <ul class="contact">
      <li><svg viewBox="0 0 10 10"><path fill="var(--green)" d="M2 1l2 2-1 1.2c.6 1.2 1.6 2.2 2.8 2.8L7 6l2 2-1.3 1.3C4.5 9 1 5.5.7 2.3z"/></svg>905-555-0142</li>
      <li><svg viewBox="0 0 10 10"><rect x="0.5" y="2" width="9" height="6" fill="var(--green)"/><path d="M0.5 2l4.5 3.5L9.5 2" stroke="#fff" fill="none"/></svg>info@brambleford.ca</li>
      <li><svg viewBox="0 0 10 10"><circle cx="5" cy="5" r="4.5" fill="var(--green)"/><path d="M1 5h8M5 .5v9" stroke="#fff" stroke-width=".8"/></svg>www.brambleford.ca</li>
    </ul>
    <span class="divider second"></span>
    <address class="address">48 Alder Street West<br>Suite 1210<br>Hamilton, ON L8P 2B7, Canada</address>
  </header>

  <h1 class="salutation">Dear Mr. Ellison,</h1>
  <section class="body-copy">
    <p>Lorem ipsum dolor sit amet, consectetuer adipiscing elit, sed diam nonmmy nibh euismod tincidunt ut laor<br>eet dolore magna aliquam erat volutpat. Ut wisi enim ad minim veniam, quis nostrud exerci tationmcorper<br>suscipit lobortis nisl ut aliquip ex ea commodo consequat. Duis autem vel eum iriure dolor in hendrerit in<br>vulputate velit esse molestie consequat, vel illum dolore eu feugiat</p>
    <p>Rorem ipsum dolor sit amet, consectetuer adipiscing elit, sed diam nonmmy nibh euismod tincidunt ut laor<br>eet dolore magna aliquam erat volutpat. Ut wisi enim ad minim veniam, quis nostrud exerci tationmcorper<br>suscipit lobortis nisl ut aliquip ex ea commodo consequat. Duis autem vel eum iriure dolor in hendrerit in<br>vulputate velit esse molest</p>
    <p>Dorem ipsum dolor sit amet, consectetuer adipiscing elit, sed diam nonmmy nibh euismod tincidunt ut laor<br>eet dolore magna aliquam erat volutpat. Ut wisi enim ad minim veniam, quis nostrud exerci tationmcorper<br>suscipit lobortis nisl ut aliquip ex ea commodo consequat. Duis autem vel eum iriure dolor in hendrerit in<br>suscipit lobortis nisl ut aliquip ex ea commodo consequat. Duis autem vel eum iriure dolor in hendrerit in<br>vulputate velit esse molestie consequat, vel illum</p>
    <p>Sorem ipsum dolor sit amet, consectetuer adipiscing elit, sed diam nonmmy nibh euismod tincidunt ut laor<br>eet dolore magna aliquam erat volutpat. Ut wisi enim ad minim veniam, quis nostrud exerci tationmcorper<br>suscipit lobortis nisl ut aliquip ex ea commodo consequat. Duis autem vel eum iriure dolor in</p>
  </section>
  <p class="closing">Sincerely,</p>

  <div class="signature-mark" role="img" aria-label="Handwritten signature of the sender"></div>
  <div class="signatory">
    <div class="signatory-name">Owen R. Brambleford</div>
    <div>Brambleford Law Professional Corporation</div>
  </div>

  <footer>
    <div class="footer-bar black"></div>
    <div class="footer-bar green"></div>
  </footer>
</main>
</body>
</html>
```